ebook cover: book 4 in the You Grow Pepper series. Warmth Beyond Fences

I am wanting a striking cover to bring the forth book in a spiritual journey series to an audience ready to meet new characters and get excited again! White backgrounds, red titles (any font), subtitles to introduce a new major character in the series of ten (same fonts please as the original, You Grow Pepper), and one emblematic, slightly mysterious image. Please keep to the same colour tones as the original, but the lead image need not be gray. Let's please try to use the "light flash" that is on the tin can in You Grow Pepper somehow, in your own way. It is meant to signify the other side, or the higher light, or some such inference.

Book details:
Title: Warmth Beyond Fences
Subtitle: Elder Corvanel brings the message
Image: silver hourglass
Author: Mabel Quinlow, Ph.D
Strap quote: "Quinlow is smart, savvy and full of ideas," Harwick Evening Ledger

Please do your best: this one is going in competition of spiritual healers!

Thanks! :)

```html
<!DOCTYPE html>
<html lang="en">
<head>
<meta charset="utf-8">
<title>Warmth Beyond Fences — Mabel Quinlow Ph.D.</title>
<link rel="stylesheet" href="https://fonts.googleapis.com/css2?family=Poppins:wght@400;600;800&family=Open+Sans:wght@600&family=Questrial&display=swap">
<style>
  :root {
    --paper: #f3f6f8;
    --title-red: #b5121b;
    --ink: #1e1f22;
    --author-grey: #6b6d70;
    --glass-light: #fbfcfd;
    --glass-mid: #eef1f3;
    --silver: #c9cdd1;
    --flash-core: #fff6c8;
    --flash-gold: #f2c230;
  }
  * { margin: 0; padding: 0; box-sizing: border-box; }
  html, body { width: 811px; height: 1200px; overflow: hidden; background: var(--paper); }
  .cover {
    position: relative;
    width: 811px;
    height: 1200px;
    background: var(--paper);
    text-align: center;
    color: var(--ink);
  }
  .strap-quote {
    position: absolute;
    top: 38px;
    left: 0;
    width: 100%;
    font-family: "Poppins", sans-serif;
    font-weight: 600;
    font-size: 13.5px;
    line-height: 22px;
    letter-spacing: 0.2px;
  }
  .strap-quote .source { font-size: 16px; font-weight: 600; }
  .title {
    position: absolute;
    top: 108px;
    left: 0;
    width: 100%;
    color: var(--title-red);
    font-family: "Poppins", sans-serif;
  }
  .title-lead {
    display: block;
    font-weight: 400;
    font-size: 56px;
    line-height: 64px;
    letter-spacing: 0.5px;
  }
  .title-main {
    display: block;
    font-weight: 800;
    font-size: 106px;
    line-height: 100px;
    letter-spacing: 1px;
  }
  .subtitle {
    position: absolute;
    top: 284px;
    left: 0;
    width: 100%;
    font-family: "Open Sans", sans-serif;
    font-weight: 600;
    font-size: 35px;
    line-height: 48px;
    letter-spacing: 8px;
    padding-left: 8px;
  }
  .lead-image {
    position: absolute;
    left: 282px;
    top: 452px;
    width: 248px;
    height: 596px;
  }
  .author {
    position: absolute;
    top: 1082px;
    left: 0;
    width: 100%;
    font-family: "Questrial", sans-serif;
    font-size: 52px;
    letter-spacing: 1px;
    color: var(--author-grey);
  }
  .author .degree { font-size: 38px; letter-spacing: 1px; }
</style>
</head>
<body>
  <main class="cover">
    <p class="strap-quote">“QUINLOW IS SMART, SAVVY AND FULL OF IDEAS!”<br><span class="source">- HARWICK EVENING LEDGER</span></p>

    <h1 class="title">
      <span class="title-lead">WARMTH BEYOND</span>
      <span class="title-main">FENCES</span>
    </h1>

    <h2 class="subtitle">ELDER CORVANEL<br>BRINGS THE MESSAGE</h2>

    <svg class="lead-image" viewBox="0 0 248 596" role="img" aria-label="Silver-framed hourglass with white sand, a golden flash of higher light glowing at its top">
      <defs>
        <linearGradient id="silver-tone" x1="0" y1="0" x2="1" y2="0">
          <stop offset="0" stop-color="var(--silver)"/>
          <stop offset="0.12" stop-color="var(--glass-mid)"/>
          <stop offset="0.5" stop-color="var(--glass-light)"/>
          <stop offset="0.88" stop-color="var(--glass-mid)"/>
          <stop offset="1" stop-color="var(--silver)"/>
        </linearGradient>
        <radialGradient id="light-flash" cx="0.5" cy="0.03" r="0.6" gradientTransform="translate(0.5 0.03) scale(1 0.45) translate(-0.5 -0.03)">
          <stop offset="0" stop-color="var(--flash-core)" stop-opacity="1"/>
          <stop offset="0.12" stop-color="var(--flash-gold)" stop-opacity="0.85"/>
          <stop offset="0.45" stop-color="var(--flash-gold)" stop-opacity="0.18"/>
          <stop offset="1" stop-color="var(--flash-gold)" stop-opacity="0"/>
        </radialGradient>
      </defs>
      <rect x="0" y="0" width="248" height="596" rx="3" fill="url(#silver-tone)"/>
      <rect x="0" y="0" width="248" height="596" rx="3" fill="url(#light-flash)"/>
    </svg>

    <p class="author">MABEL QUINLOW P<span class="degree">H.D.</span></p>
  </main>
</body>
</html>
```